依頼詳細
コンテストは、対象であるミドル・シニアで65歳以上の方が、ご自身が撮影した作品、もしくはご自身が出演する作品を、「どきどきする動画」をテーマとして応募頂きます。
ミドル・シニアの方々の「人生経験」が「人気コンテンツ」に変わる瞬間や、これまでの動画を見る立場から、動画を制作し参加する側へ誘うきっかけになればと思っております。
また、賞金総額が2部門で100万円と高額なコンテストとなっており、そうしたあおり文句も前面に出していただけるチラシにしたいです。
記載項目
コンテストタイトル:S70 全国 ぽかCaster コンテスト
ヘッドコピー:」どきどきする動画を大募集
煽りコピー:グランプリ賞金総額100万円
その他、・応募要項・審査の流れ・表彰概要・応募方法・問い合わせ先
は必須項目として掲載したいです。
*一部詳細は、添付のPPTをご確認ください。
サイズ
A4
ページ数
片面
希望イメージ
シンプル 複雑
単色 カラフル
暗い 明るい
日常 高級
遊び心 厳粛
未来的 伝統的
女性的 男性的
希望する色
赤系、黄・オレンジ系、茶系
納品ファイル
• イラストレーター形式 (.ai)
補足説明
弊社ホームページ
https://nq-lp.com/
■ 選んだ理由

社内で協議の結果。

■ 提案者全員のお礼・コメント

皆様から頂いた案件を、
社内で協議して、社員の総意で決定しました。ありがとうございました。

```html
<!DOCTYPE html>
<html lang="ja">
<head>
<meta charset="UTF-8">
<title>S70 全国ぽかCasterコンテスト</title>
<link href="https://fonts.googleapis.com/css2?family=M+PLUS+Rounded+1c:wght@500;800;900&family=Noto+Sans+JP:wght@400;700;900&display=swap" rel="stylesheet">
<style>
  :root {
    --yellow: #f5d031;
    --yellow-light: #f8e36a;
    --cream: #fffbea;
    --ink: #3a2a18;
    --white: #ffffff;
    --photo-warm: #c9a57a;
    --photo-cool: #9fb3c4;
  }
  html, body { margin: 0; padding: 0; overflow: hidden; }
  body { width: 849px; height: 1200px; background: var(--white); }
  .poster {
    position: relative; width: 849px; height: 1200px; overflow: hidden;
    background: var(--white); color: var(--ink);
    font-family: "Noto Sans JP", sans-serif;
  }
  .backdrop { position: absolute; inset: 0; }
  .prize-banner { position: absolute; left: 26px; top: 24px; width: 430px; }
  .prize-banner__lead {
    font-family: "M PLUS Rounded 1c", sans-serif; font-weight: 800;
    font-size: 40px; color: var(--cream); letter-spacing: 2px; margin: 0;
    text-shadow: 0 0 2px var(--ink);
  }
  .prize-banner__amount {
    font-family: "M PLUS Rounded 1c", sans-serif; font-weight: 900;
    font-size: 84px; line-height: 1; color: var(--white); margin: 4px 0 14px;
    text-shadow: 0 0 3px var(--ink);
  }
  .schedule { margin: 0; padding: 0; list-style: none; font-size: 14px; line-height: 1.75; font-weight: 700; }
  .catch {
    position: absolute; left: 260px; top: 312px; width: 560px; margin: 0;
    transform: rotate(-3deg);
    font-family: "M PLUS Rounded 1c", sans-serif; font-weight: 900;
    font-size: 42px; letter-spacing: 2px; color: var(--white);
    -webkit-text-stroke: 7px var(--ink); paint-order: stroke fill;
  }
  .title {
    position: absolute; left: 300px; top: 420px; width: 520px; margin: 0;
    font-family: "M PLUS Rounded 1c", sans-serif; font-weight: 900;
    color: var(--ink); line-height: 1.05; text-align: center;
  }
  .title__code { display: block; font-size: 62px; margin-left: -90px; }
  .title__name { display: block; font-size: 64px; }
  .title__tail { display: block; font-size: 74px; margin-left: 40px; }
  .info-column {
    position: absolute; writing-mode: vertical-rl; text-orientation: mixed; margin: 0;
    font-size: 13px; line-height: 1.7; color: var(--ink);
  }
  .info-column__heading {
    font-family: "Noto Sans JP", sans-serif; font-weight: 900;
    font-size: 22px; line-height: 1.3; letter-spacing: 4px;
    margin: 0 0 0 14px; padding: 0;
  }
  .info-column p { margin: 0; }
  .requirements { right: 70px; top: 640px; height: 430px; }
  .awards { left: 400px; top: 650px; height: 430px; }
  .judging { left: 230px; top: 690px; height: 380px; }
  .how-to { left: 40px; top: 800px; height: 290px; }
  .contact-bar {
    position: absolute; left: 0; right: 0; bottom: 0; height: 44px;
    display: flex; justify-content: space-between; align-items: center;
    padding: 0 36px; font-size: 15px; font-weight: 700; color: var(--ink);
  }
  .contact-bar__company { display: flex; gap: 40px; }
</style>
</head>
<body>
<main class="poster">
  <svg class="backdrop" width="849" height="1200" viewBox="0 0 849 1200">
    <defs>
      <linearGradient id="g-active" x1="0" y1="0" x2="1" y2="1">
        <stop offset="0" stop-color="#e9dccb"/><stop offset="0.5" stop-color="#c9a57a"/><stop offset="1" stop-color="#7d8e9c"/>
      </linearGradient>
      <linearGradient id="g-couple" x1="0" y1="0" x2="0" y2="1">
        <stop offset="0" stop-color="#cfdbe6"/><stop offset="0.55" stop-color="#9fb3c4"/><stop offset="1" stop-color="#8a7763"/>
      </linearGradient>
    </defs>
    <circle cx="460" cy="1010" r="440" fill="#f8e36a"/>
    <circle cx="650" cy="140" r="270" fill="#f5d031"/>
    <circle cx="650" cy="140" r="250" fill="url(#g-active)" role="img" aria-label="笑顔でストレッチをするシニアの男女の写真"/>
    <path d="M0 0 H470 V170 Q470 285 340 285 H0 Z" fill="#f5d031"/>
    <circle cx="150" cy="365" r="200" fill="#f5d031"/>
    <circle cx="150" cy="365" r="184" fill="url(#g-couple)" role="img" aria-label="ベンチに並んで座る高齢の夫婦の後ろ姿の写真"/>
    <rect x="0" y="1156" width="849" height="44" fill="#f5d031"/>
  </svg>

  <header class="prize-banner">
    <p class="prize-banner__lead">グランプリ賞金総額</p>
    <p class="prize-banner__amount">100万円</p>
    <ul class="schedule">
      <li>応募期間：2021.○.○(○○の日)～2021.○.○締切</li>
      <li>入賞者発表：2021.○.○(○○の日)</li>
      <li>授賞式：2022.○.○</li>
    </ul>
  </header>

  <p class="catch">どきどきする動画を大募集</p>

  <h1 class="title">
    <span class="title__code">S70</span>
    <span class="title__name">全国ぽかCaster</span>
    <span class="title__tail">コンテスト</span>
  </h1>

  <section class="info-column requirements">
    <h2 class="info-column__heading">応募要項</h2>
    <p>・６５歳以上のミドル・シニアの方</p>
    <p>・ご自身が撮影、または出演する作品</p>
    <p>・テーマは「どきどきする動画」</p>
    <p>・動画は○分以内、お一人○作品まで</p>
    <p>・未発表のオリジナル作品に限ります</p>
  </section>

  <section class="info-column awards">
    <h2 class="info-column__heading">表彰概要</h2>
    <p>・グランプリ　賞金○○万円（各部門一名）</p>
    <p>・準グランプリ　賞金○○万円（各一名）</p>
    <p>・優秀賞　賞金○万円（各○名）</p>
    <p>・審査員特別賞　記念品（○名）</p>
    <p>・入賞作品はサイトで公開します</p>
  </section>

  <section class="info-column judging">
    <h2 class="info-column__heading">審査の流れ</h2>
    <p>・一次審査　○月○日</p>
    <p>・二次審査　○月○日</p>
    <p>・最終審査　○月○日</p>
    <p>・結果発表　○月○日</p>
  </section>

  <section class="info-column how-to">
    <h2 class="info-column__heading">応募方法</h2>
    <p>・コンテストサイトより</p>
    <p>　https://poka-contest.jp/</p>
    <p>・必要事項を入力し投稿</p>
  </section>

  <footer class="contact-bar">
    <span>お問い合わせ：〒100-0000 東京都千代田区○○</span>
    <span class="contact-bar__company"><span>株式会社 ○○○</span><span>TEL ○○○○○○</span></span>
  </footer>
</main>
</body>
</html>
```